Verpackungsdesign für Menstruationstasse gesucht
Zielgruppe
wir sind Hersteller von nachhaltige Damenhygieneartikeln. Wir suchen ein hochwertiges Design für unsere neue Verpackung. Wir legen großen Wert auf Nachhaltigkeit. Zielgruppe sind Frauen im Gebärfähigen Alter, welche Wert auf ihre Gesundheit und die Umwelt legen.
Aufgabenstellung
> Ein Bild der Menstruationstasse sollte auf der Verpackung außen sichtbar sein, weil wir kein Fenster im Karton haben.
> wir brauchen ein Markiertes Feld auf dem Karton mit freier Fläche um einen Aufkleber mit EAN code platzieren zu können.
> Der Karton ist matt-weiß.
>Auf der Frontseite sollte das Logo und ein Schriftzug mit 'Menstruationstasse' sein.
> Generell sollte gut auf einen Blick ersichtlich sein, dass die Cup in Deutschland produziert wird.
> Das Logo wird in UV-Lack gedruckt.

```html
<!DOCTYPE html>
<html lang="de">
<head>
<meta charset="utf-8">
<title>VENA Menstruationstasse – Verpackung</title>
<link href="https://fonts.googleapis.com/css2?family=Quicksand:wght@500;600;700&display=swap" rel="stylesheet">
<style>
  :root {
    --backdrop: #eeeef1;
    --carton: #ffffff;
    --ink: #1e1e22;
    --berry: #c4507a;
    --mint: #7ecbc0;
    --cup-tone: #f1f1f3;
    --flag-black: #141414;
    --flag-red: #dd1f26;
    --flag-gold: #ffce00;
  }
  * { box-sizing: border-box; margin: 0; padding: 0; }
  html, body { width: 1200px; height: 1200px; overflow: hidden; }
  body {
    background: var(--backdrop);
    font-family: "Quicksand", sans-serif;
    color: var(--ink);
    position: relative;
  }
  .panel {
    position: absolute;
    top: 45px;
    width: 380px;
    height: 1110px;
    background: var(--carton);
    box-shadow: 0 6px 24px rgba(0,0,0,0.10);
    overflow: hidden;
  }
  .panel--side { left: 170px; }
  .panel--front { left: 650px; }

  .brand {
    position: absolute;
    top: 42px; left: 0; right: 0;
    text-align: center;
    font-weight: 700;
    font-size: 84px;
    letter-spacing: 0.12em;
    color: var(--berry);
    line-height: 1;
  }
  .product-title {
    position: absolute;
    top: 163px; left: 0; right: 0;
    text-align: center;
    font-weight: 500;
    font-size: 22px;
    letter-spacing: 0.12em;
  }

  .facts { position: absolute; top: 254px; left: 0; right: 8px; }
  .fact { margin-bottom: 20px; }
  .tag {
    display: inline-block;
    padding: 0 22px 0 21px;
    height: 15px;
    line-height: 15px;
    font-size: 14px;
    font-weight: 600;
    letter-spacing: 0.08em;
    color: #fff;
    border-radius: 0 8px 8px 0;
  }
  .tag--berry { background: var(--berry); }
  .tag--mint { background: var(--mint); }
  .tag-stack .tag { display: table; margin-bottom: 2px; }
  .fact p {
    padding-left: 39px;
    font-size: 15.5px;
    line-height: 18.5px;
    letter-spacing: 0.06em;
    font-weight: 500;
  }
  .contents { position: relative; }
  .contents .mini-cup {
    position: absolute; right: 36px; top: 0;
    width: 26px; height: 50px;
    background: linear-gradient(#e4e4e8, #cfcfd5);
    border-radius: 4px 4px 12px 12px;
  }

  .imprint {
    position: absolute;
    left: 21px; bottom: 20px;
    font-size: 15.5px;
    line-height: 24px;
    letter-spacing: 0.06em;
    font-weight: 600;
  }

  .cup-view {
    position: absolute;
    top: 231px; left: 61px;
    width: 258px; height: 522px;
    background: linear-gradient(180deg, var(--cup-tone), #e2e2e6);
    border-radius: 18px 18px 40% 40% / 18px 18px 30% 30%;
  }
  .variant { position: absolute; left: 0; right: 0; }
  .variant--type { top: 820px; }
  .variant--size { top: 899px; }
  .variant p {
    padding-left: 37px;
    margin-top: 4px;
    font-size: 15.5px;
    line-height: 19px;
    letter-spacing: 0.06em;
    font-weight: 500;
  }
  .tag--wide { width: 180px; }
  .tag--wide span { margin-left: 40px; }

  .colour-note {
    position: absolute;
    left: 22px; bottom: 38px;
    display: flex; align-items: center; gap: 28px;
    font-size: 14px; font-weight: 600; letter-spacing: 0.08em;
  }
  .colour-swatch {
    width: 14px; height: 40px;
    background: var(--berry);
    border-radius: 3px 3px 7px 7px;
  }
  .flag-corner { position: absolute; right: 0; bottom: 0; width: 95px; height: 95px; }
</style>
</head>
<body>

<section class="panel panel--side">
  <div class="brand">VENA</div>
  <div class="product-title">MENSTRUATIONSTASSE</div>

  <div class="facts">
    <div class="fact contents">
      <span class="tag tag--berry">Inhalt:</span>
      <p>Menstruationstasse<br>Gebrauchsanleitung</p>
      <div class="mini-cup" role="img" aria-label="Kleine Skizze der Menstruationstasse"></div>
    </div>
    <div class="fact">
      <span class="tag tag--mint">Plastikfrei:</span>
      <p>Umweltschutz wird bei VENA großgeschrieben. Wir verkaufen unsere Produkte komplett plastikfrei.</p>
    </div>
    <div class="fact">
      <span class="tag tag--mint">Deutsche Produktion:</span>
      <p>Venacup wird in Deutschland,<br>aus deutschem Silikon hergestellt.<br>Sie ist absolut frei von Giftstoffen<br>wie z.B. Weichmachern oder Dioxin.</p>
    </div>
    <div class="fact">
      <span class="tag tag--mint">Höchste Qualität:</span>
      <p>Venacup wird aus 100% medizinisch<br>zertifiziertem Silikon hergestellt.</p>
    </div>
    <div class="fact">
      <span class="tag tag--mint">Kürzbarer Stiel:</span>
      <p>Wenn du möchtest, kannst du<br>den Stiel bei Bedarf abschneiden.</p>
    </div>
    <div class="fact">
      <span class="tag tag--mint">Nahtlose Oberfläche:</span>
      <p>Venacup hat keine störende Naht,<br>durch die Formtrennung an der<br>Oberfläche.</p>
    </div>
    <div class="fact tag-stack">
      <span class="tag tag--mint">Speziell auch für</span>
      <span class="tag tag--mint">Menstruationstassen-Anfängerinnen</span>
      <span class="tag tag--mint">geeignet:</span>
      <p>Venacup ist besonders leicht<br>in der Handhabnung, da sie sich<br>im Vergleich zu vielen anderen Cups<br>besonders gut entfalten lässt.</p>
    </div>
  </div>

  <address class="imprint" style="font-style:normal">
    Vena Öko Handels GmbH<br>
    am Lindenhang 7/2<br>
    72108 Brunnfeld<br>
    Email: kontakt@venacup.de<br>
    www.venacup.de
  </address>

  <svg class="flag-corner" viewBox="0 0 95 95" aria-hidden="true">
    <polygon points="95,0 95,38 38,95 0,95" fill="var(--flag-black)"/>
    <polygon points="95,38 95,68 68,95 38,95" fill="var(--flag-red)"/>
    <polygon points="95,68 95,95 68,95" fill="var(--flag-gold)"/>
  </svg>
</section>

<section class="panel panel--front">
  <div class="brand">VENA</div>
  <div class="product-title">MENSTRUATIONSTASSE</div>

  <div class="cup-view" role="img" aria-label="Linienzeichnung der Menstruationstasse mit Stiel"></div>

  <div class="variant variant--type">
    <span class="tag tag--berry tag--wide">classic (weich)</span>
    <p>Geeignet für Frauen mit mittelstarker<br>Beckenbodenmuskulatur.</p>
  </div>
  <div class="variant variant--size">
    <span class="tag tag--mint tag--wide">Größe<span>1</span></span>
    <p>Geeignet für Frauen mit 0-1 Geburten</p>
  </div>

  <div class="colour-note">
    <span>FARBE:</span>
    <span class="colour-swatch" role="img" aria-label="Farbmuster der Tasse in Beere"></span>
  </div>

  <svg class="flag-corner" viewBox="0 0 95 95" aria-hidden="true">
    <polygon points="95,0 95,38 38,95 0,95" fill="var(--flag-black)"/>
    <polygon points="95,38 95,68 68,95 38,95" fill="var(--flag-red)"/>
    <polygon points="95,68 95,95 68,95" fill="var(--flag-gold)"/>
  </svg>
</section>

</body>
</html>
```